Dorian Walsby Psychotherapy Business Card Design Project

I need a welcoming business card for a Somatic Psychotherapy private practice based in Melbourne, Australia. I help individual clients to work through issues in their life that are inhibiting achieving their full potential. I would like a san serif font and the oculars are:
blue: R:37 G:61 B:95 C:93 M:77 Y:38 K:28
orange: R:241 G:103 B:43 C:0 M:74 Y:93 K:0
The final design should communicate warm, welcoming and safe environment in which clients are supported to grow. It should also convey a collaborative approach to achieve success between me (the therapist) and the client. The uploaded file is my new logo. Also an organic look and feel while maintaining professionalism and a clean, simple look is sought after.
In addition to the logo my details are:
Dorian Walsby
Psychotherapist
B.Arts., Grad Dip. T&D., Dip.Som.Psych, MRKTA, MLOHVB
0417 582 930
dwalsby@dorianwalsby.com.au
www.dorianwalsby.com.au
Target Market(s)
Psychotherapy Clients
Industry/Entity Type
Environment

```html
<!DOCTYPE html>
<html lang="en">
<head>
<meta charset="utf-8">
<title>Dorian Walsby Psychotherapy – Business Card</title>
<link rel="stylesheet" href="https://fonts.googleapis.com/css2?family=Open+Sans:wght@400;600&display=swap">
<style>
  :root {
    --brand-blue: #253d5f;
    --brand-orange: #f1672b;
    --card-dark: #2b2220;
    --card-light: #ededed;
    --card-white: #f4f4f4;
    --rule-light: #b9b9b9;
    --rule-dark: #6b5f5b;
    --text-light: #f2f2f2;
    --stage: #1d1d1f;
  }
  * { box-sizing: border-box; margin: 0; padding: 0; }
  html, body { width: 1200px; height: 800px; overflow: hidden; }
  body {
    background: var(--stage);
    font-family: "Open Sans", Arial, sans-serif;
    position: relative;
  }
  .card {
    position: absolute;
    top: 250px;
    width: 490px;
    height: 296px;
    overflow: hidden;
    box-shadow: 0 10px 30px rgba(0,0,0,.55);
  }
  .card--front { left: 80px; background: var(--card-dark); }
  .card--back  { left: 630px; background: var(--card-light); }

  /* Wordmark */
  .wordmark {
    display: flex;
    align-items: center;
    justify-content: center;
    gap: 12px;
    font-weight: 600;
    letter-spacing: .2px;
    white-space: nowrap;
  }
  .wordmark__dot {
    width: 34px; height: 34px;
    border-radius: 50%;
    background: var(--brand-orange);
    flex: none;
  }

  /* Front */
  .front__header {
    height: 100px;
    background: var(--card-white);
    display: flex;
    align-items: center;
    justify-content: center;
  }
  .front__header .wordmark { color: var(--brand-blue); font-size: 26px; }
  .front__rule {
    height: 12px;
    background: var(--card-white);
    border-top: 1px dashed var(--rule-light);
    border-bottom: 3px solid #d9d9d9;
  }
  .front__body {
    padding-top: 22px;
    text-align: center;
    color: var(--text-light);
  }
  .front__name { font-size: 19px; font-weight: 400; }
  .front__title {
    font-size: 13px;
    font-weight: 600;
    color: var(--brand-orange);
    margin-top: 1px;
  }
  .front__underline {
    width: 54px; height: 2px;
    background: var(--brand-orange);
    margin: 6px auto 16px;
  }
  .contact-list { list-style: none; display: inline-block; text-align: left; }
  .contact-list li {
    display: flex; align-items: center; gap: 8px;
    font-size: 14px; line-height: 22px;
  }
  .contact-list svg { width: 13px; height: 13px; flex: none; }

  /* Back */
  .back__top { height: 62px; }
  .back__band {
    position: relative;
    height: 102px;
    background: var(--card-dark);
    display: flex; align-items: center; justify-content: center;
    box-shadow: 0 -7px 0 -3px var(--card-light), 0 7px 0 -3px var(--card-light);
  }
  .back__band::before, .back__band::after {
    content: ""; position: absolute; left: 0; right: 0;
    border-top: 1px dashed var(--rule-dark);
  }
  .back__band::before { top: 6px; }
  .back__band::after { bottom: 6px; }
  .back__band .wordmark { color: var(--brand-orange); font-size: 28px; }
  .back__rule {
    height: 10px;
    border-bottom: 1px dashed var(--rule-light);
  }
  .credentials {
    margin: 22px 16px 0;
    height: 34px;
    border-radius: 17px;
    background: #e2e2e2;
    box-shadow: inset 0 1px 2px rgba(0,0,0,.15);
    display: flex; align-items: center; justify-content: center;
    font-size: 12.5px; font-weight: 600;
    color: var(--brand-blue);
    white-space: nowrap;
  }
</style>
</head>
<body>

  <article class="card card--front" aria-label="Business card front">
    <header class="front__header">
      <div class="wordmark"><span class="wordmark__dot"></span>Dorian Walsby Psychotherapy</div>
    </header>
    <div class="front__rule"></div>
    <section class="front__body">
      <h1 class="front__name">Dorian Walsby</h1>
      <p class="front__title">Psychotherapist</p>
      <div class="front__underline"></div>
      <ul class="contact-list">
        <li>
          <svg viewBox="0 0 16 16" aria-hidden="true"><circle cx="8" cy="8" r="8" fill="#f2f2f2"/><path d="M5.2 4.2l1.4-.2.8 1.9-.9.8a5 5 0 0 0 2.8 2.8l.8-.9 1.9.8-.2 1.4c-3.6.3-6.9-3-6.6-6.6z" fill="#2b2220"/></svg>
          0417 582 930
        </li>
        <li>
          <svg viewBox="0 0 16 16" aria-hidden="true"><circle cx="8" cy="8" r="8" fill="#f2f2f2"/><rect x="4" y="5.2" width="8" height="5.6" fill="#2b2220"/><path d="M4 5.4l4 3 4-3" stroke="#f2f2f2" stroke-width=".9" fill="none"/></svg>
          dwalsby@dorianwalsby.com.au
        </li>
        <li>
          <svg viewBox="0 0 16 16" aria-hidden="true"><circle cx="8" cy="8" r="8" fill="#f2f2f2"/><circle cx="8" cy="8" r="4" fill="none" stroke="#2b2220" stroke-width="1"/><path d="M4 8h8M8 4c-2 2.4-2 5.6 0 8M8 4c2 2.4 2 5.6 0 8" stroke="#2b2220" stroke-width=".8" fill="none"/></svg>
          www.dorianwalsby.com.au
        </li>
      </ul>
    </section>
  </article>

  <article class="card card--back" aria-label="Business card back">
    <div class="back__top"></div>
    <section class="back__band">
      <div class="wordmark"><span class="wordmark__dot"></span>Dorian Walsby Psychotherapy</div>
    </section>
    <div class="back__rule"></div>
    <p class="credentials">B.Arts., Grad Dip. T&amp;D., Dip.Som.Psych, MRKTA, MLOHVB</p>
  </article>

</body>
</html>
```